Web Design Project for DJ

We need a web design for a DJ. Our client is a freelance DJ who already has a regular gig at a major night club but is looking to expand his exposure. He is located in a major metropolitan area and is looking for further gigs. He is hoping to generate further business via the website, including bookings via the site.

For reference his pagelinker page is here https://www.pagelinker.example/pages/DJ-Vorn/730162948415207

Following face to face discussions with the client today we have made a few small alterations to the brief.  We are hoping to have some images uploaded shortly.

Target Market(s)

Event planners, night club owners, radio stations, younger age groups (16-35)

Industry/Entity Type

Business

Requirements
Must have
• Name is DJVorn, this should obviously feature prominently. His current business card is attached as an example.

Links to Pagelinker and Tunedrift

Cool, modern look, slightly edgy.

Site will be built in Joomla, so a front page and secondary page template is required.
Nice to have
• Blog style layout to front page featuring recent and upcoming gigs.

Secondary pages may include a more expansive blog, a list of upcoming gigs, and a booking form.

Darker colour palettes preferred and use of same/similar fonts to those on the business card are an obvious plus

```html
<!DOCTYPE html>
<html lang="en">
<head>
<meta charset="utf-8">
<title>DJ VORN</title>
<link href="https://fonts.googleapis.com/css2?family=Lato:wght@400;700;900&display=swap" rel="stylesheet">
<style>
:root{
  --page:#151515;
  --panel:#1d1d1d;
  --card:#262626;
  --line:#333333;
  --blue:#1f7fd6;
  --blue-dark:#1766b0;
  --white:#ffffff;
  --text:#d6d6d6;
  --muted:#9a9a9a;
  --orange:#f26a1b;
}
*{margin:0;padding:0;box-sizing:border-box}
html,body{width:1200px;height:2289px;overflow:hidden}
body{background:var(--page);font-family:'Lato',Arial,sans-serif;color:var(--text);position:relative}
.abs{position:absolute}
.bar-top{left:0;top:0;width:1200px;height:7px;background:var(--blue)}
.page{left:48px;top:7px;width:1106px;height:1887px;background:var(--panel)}
.brand{left:88px;top:48px;display:flex;align-items:center;gap:12px}
.brand-mark{width:22px;height:22px;background:var(--blue)}
.brand-name{font-size:40px;font-weight:700;color:var(--white);line-height:1}
.nav{right:78px;top:52px;display:flex;gap:22px;font-size:21px;font-weight:700;color:var(--white)}
.slider{left:82px;top:135px;width:1042px;height:525px;background:radial-gradient(ellipse at 50% 40%,#8a8a8a 0%,#4a4a4a 45%,#1b1b1b 100%)}
.slider-arrow{top:385px;width:30px;height:30px;border-radius:50%;background:rgba(0,0,0,.45)}
.dots{left:570px;top:682px;display:flex;gap:5px}
.dots i{width:11px;height:11px;border-radius:50%;background:#050505;display:block}
.dots i.on{background:var(--blue)}
.section-title{font-size:27px;font-weight:900;color:var(--white);text-transform:uppercase}
.event{top:757px;height:132px;width:344px;background:var(--card);border:1px solid var(--line);display:flex}
.event-date{width:110px;background:var(--blue);color:var(--white);text-align:center;display:flex;flex-direction:column;justify-content:center;font-weight:700;line-height:1.1}
.event-date .big{font-size:38px}
.event-date .mid{font-size:22px}
.event-info{padding:12px 12px}
.event-venue{font-size:17px;color:var(--blue-dark)}
.event-city{font-size:20px;font-weight:700;color:var(--white);margin-top:12px;line-height:1}
.btn{display:inline-block;margin-top:16px;padding:5px 8px;font-size:16px;font-weight:700;background:var(--blue);color:var(--white)}
.btn.sold{background:#4a4a4a;color:#6e6e6e}
.player{left:88px;top:977px;width:347px;height:263px;background:#f6f6f6;border-radius:6px;color:#333}
.play{left:14px;top:22px;width:64px;height:64px;border-radius:50%;background:var(--orange)}
.who{left:92px;top:34px;font-size:17px;color:#555}
.track{left:92px;top:58px;font-size:21px;font-weight:700;color:#333}
.buy{left:300px;top:60px;font-size:17px;color:#666}
.pbtn{top:16px;width:36px;height:30px;border:1px solid #ccc;border-radius:4px;background:#fff}
.wave{left:12px;top:110px}
.stats{left:18px;top:228px;font-size:16px;color:#888;display:flex;gap:20px}
.video{left:88px;width:345px;background:var(--card);border:1px solid var(--line)}
.video-img{width:100%;height:192px;position:relative}
.video-play{position:absolute;left:50%;top:50%;width:92px;height:92px;margin:-46px 0 0 -46px;border-radius:50%;background:rgba(0,0,0,.65)}
.video-cap{padding:20px 16px;font-size:18px;color:var(--white)}
.news-img{left:487px;top:973px;width:635px;height:416px;background:radial-gradient(ellipse at 50% 45%,#c9a68e 0%,#e9e4e0 55%,#f2f2f2 100%)}
.news-meta{left:487px;top:1415px;font-size:14px;font-weight:900;color:var(--white)}
.news-meta span{color:var(--blue);font-weight:700;margin-left:12px}
.news-text{left:487px;top:1456px;width:635px;font-size:17.5px;line-height:1.55;color:var(--white)}
.readmore{left:487px;top:1620px;font-size:19px;font-weight:700;color:var(--blue)}
.divider{left:487px;top:1660px;width:635px;height:3px;background:#2c2c2c}
.news-img2{left:487px;top:1711px;width:635px;height:183px;background:linear-gradient(135deg,#5a1f7a 0%,#a33fb8 50%,#3a1650 100%)}
.footer-line{left:0;top:1894px;width:1200px;height:5px;background:var(--blue)}
.footer{left:0;top:1899px;width:1200px;height:383px;background:var(--panel)}
.bar-bottom{left:0;top:2282px;width:1200px;height:7px;background:var(--blue)}
.f-title{top:1966px;font-size:17px;font-weight:700;color:#cfcfcf;text-transform:uppercase}
.f-text{top:2002px;width:256px;font-size:13.5px;font-weight:700;line-height:1.55;color:var(--white)}
.f-text p+p{margin-top:10px}
.thumb{width:70px;height:70px;border:3px solid #2e2e2e;background:linear-gradient(135deg,#8a7a62,#3d3a36)}
.cal{left:893px;top:1997px;width:262px;font-size:14px;font-weight:700;color:var(--white);border-collapse:collapse}
.cal caption{font-size:14px;padding-bottom:6px}
.cal td,.cal th{text-align:center;height:24px;font-weight:700}
.cal .prev{color:var(--blue);text-align:left}
</style>
</head>
<body>
<div class="abs bar-top"></div>
<div class="abs page"></div>

<header>
  <div class="abs brand"><span class="brand-mark"></span><span class="brand-name">DJ VORN</span></div>
  <nav class="abs nav"><span>Home</span><span>Shop</span><span>Discography</span><span>Artists</span><span>Photos</span><span>Videos</span><span>Events</span><span>Blog</span></nav>
</header>

<div class="abs slider" role="img" aria-label="Black and white photo of the DJ on stage with arms raised before a crowd"></div>
<div class="abs slider-arrow" style="left:98px"></div>
<div class="abs slider-arrow" style="left:1076px"></div>
<div class="abs dots"><i></i><i></i><i class="on"></i><i></i><i></i></div>

<h2 class="abs section-title" style="left:84px;top:705px">Upcoming Events</h2>

<div class="abs event" style="left:86px">
  <div class="event-date"><span class="mid">Every</span><span class="mid">WED</span><span class="big" style="font-size:30px">22:00</span></div>
  <div class="event-info"><div class="event-venue">Olvera Arena</div><div class="event-city">Athens,Greece</div><span class="btn">BUY NOW</span></div>
</div>
<div class="abs event" style="left:431px">
  <div class="event-date"><span class="big">11</span><span class="mid">Oct</span><span class="mid" style="font-size:26px">2013</span></div>
  <div class="event-info"><div class="event-venue">Espacio Marlo</div><div class="event-city">Santiago, Chile</div><span class="btn sold">SOLD OUT</span></div>
</div>
<div class="abs event" style="left:775px">
  <div class="event-date"><span class="big">19</span><span class="mid">Oct</span><span class="mid" style="font-size:26px">2013</span></div>
  <div class="event-info"><div class="event-venue">Brightwater Music Hall</div><div class="event-city">Amsterdam,<br>Netherlands</div><span class="btn" style="margin-top:6px">BUY TICKETS</span></div>
</div>

<h2 class="abs section-title" style="left:88px;top:925px">Tunedrift</h2>
<div class="abs player">
  <div class="abs play"><svg width="64" height="64"><polygon points="25,18 47,32 25,46" fill="#fff"/></svg></div>
  <div class="abs who">T'K</div>
  <div class="abs track">Velvet Ri...</div>
  <div class="abs pbtn" style="left:250px"><svg width="36" height="30"><path d="M18 22l-7-7a4 4 0 0 1 7-4a4 4 0 0 1 7 4z" fill="#333"/></svg></div>
  <div class="abs pbtn" style="left:292px"><svg width="36" height="30"><path d="M11 12v10h14v-6M19 9h7v7M26 9l-9 9" stroke="#333" stroke-width="2" fill="none"/></svg></div>
  <div class="abs buy">Buy</div>
  <svg class="abs wave" width="323" height="110" viewBox="0 0 323 110">
    <g fill="#555">
      <rect x="0" y="30" width="3" height="60"/><rect x="5" y="22" width="3" height="68"/><rect x="10" y="35" width="3" height="55"/><rect x="15" y="18" width="3" height="72"/><rect x="20" y="28" width="3" height="62"/><rect x="25" y="40" width="3" height="50"/><rect x="30" y="20" width="3" height="70"/><rect x="35" y="26" width="3" height="64"/><rect x="40" y="15" width="3" height="75"/><rect x="45" y="32" width="3" height="58"/><rect x="50" y="24" width="3" height="66"/><rect x="55" y="38" width="3" height="52"/><rect x="60" y="19" width="3" height="71"/><rect x="65" y="27" width="3" height="63"/><rect x="70" y="34" width="3" height="56"/><rect x="75" y="16" width="3" height="74"/><rect x="80" y="29" width="3" height="61"/><rect x="85" y="22" width="3" height="68"/><rect x="90" y="36" width="3" height="54"/><rect x="95" y="18" width="3" height="72"/><rect x="100" y="25" width="3" height="65"/><rect x="105" y="40" width="3" height="50"/><rect x="110" y="21" width="3" height="69"/><rect x="115" y="30" width="3" height="60"/><rect x="120" y="14" width="3" height="76"/><rect x="125" y="33" width="3" height="57"/><rect x="130" y="23" width="3" height="67"/><rect x="135" y="37" width="3" height="53"/><rect x="140" y="19" width="3" height="71"/><rect x="145" y="28" width="3" height="62"/><rect x="150" y="17" width="3" height="73"/><rect x="155" y="35" width="3" height="55"/><rect x="160" y="24" width="3" height="66"/><rect x="165" y="31" width="3" height="59"/><rect x="170" y="15" width="3" height="75"/><rect x="175" y="39" width="3" height="51"/><rect x="180" y="22" width="3" height="68"/><rect x="185" y="29" width="3" height="61"/><rect x="190" y="18" width="3" height="72"/><rect x="195" y="34" width="3" height="56"/><rect x="200" y="26" width="3" height="64"/><rect x="205" y="20" width="3" height="70"/><rect x="210" y="36" width="3" height="54"/><rect x="215" y="16" width="3" height="74"/><rect x="220" y="30" width="3" height="60"/><rect x="225" y="23" width="3" height="67"/><rect x="230" y="38" width="3" height="52"/><rect x="235" y="19" width="3" height="71"/><rect x="240" y="27" width="3" height="63"/><rect x="245" y="33" width="3" height="57"/><rect x="250" y="17" width="3" height="73"/><rect x="255" y="29" width="3" height="61"/><rect x="260" y="24" width="3" height="66"/>
    </g>
    <g fill="#bdbdbd">
      <rect x="265" y="34" width="3" height="56"/><rect x="270" y="26" width="3" height="64"/><rect x="275" y="38" width="3" height="52"/><rect x="280" y="30" width="3" height="60"/><rect x="285" y="42" width="3" height="48"/><rect x="290" y="32" width="3" height="58"/><rect x="295" y="40" width="3" height="50"/>
    </g>
    <rect x="282" y="68" width="38" height="20" fill="#222"/>
    <text x="288" y="83" font-family="Lato,Arial,sans-serif" font-size="13" fill="#fff">5.01</text>
  </svg>
  <div class="abs stats"><span>▶ 11,120</span><span>♥ 9</span><span>▮ 14</span></div>
</div>

<h2 class="abs section-title" style="left:88px;top:1275px">Latest Videos</h2>
<div class="abs video" style="top:1330px">
  <div class="video-img" role="img" aria-label="Festival crowd dancing with raised hands" style="background:linear-gradient(180deg,#8c9aa8,#5a4a40)"><span class="video-play"><svg width="92" height="92"><polygon points="38,28 64,46 38,64" fill="#fff"/></svg></span></div>
  <div class="video-cap">Kestro &amp; Halden</div>
</div>
<div class="abs video" style="top:1590px">
  <div class="video-img" role="img" aria-label="People dancing on a beach at sunset" style="background:linear-gradient(180deg,#4d8fd0,#e7c99a 70%,#8a6a4a)"><span class="video-play"><svg width="92" height="92"><polygon points="38,28 64,46 38,64" fill="#fff"/></svg></span></div>
  <div class="video-cap">Ibiza Beaches</div>
</div>

<h2 class="abs section-title" style="left:487px;top:925px">News</h2>
<div class="abs news-img" role="img" aria-label="Woman wearing sunglasses and headphones"></div>
<div class="abs news-meta">OCTOBER 4, 2012 &nbsp;•<span>3 COMMENTS</span></div>
<p class="abs news-text">libendum elit, eu euismod magna sapien ut nibh. Donec semper quam scelerisque tortor dictum gravida. In hac habitasse platea dictumst. Nam pulvinar, odio sed rhoncus suscipit, sem diam ultrices mauris, eu consequat purus metus eu velit. Proin metus odio, aliquam eget molestie nec, gravida ut sapien. Phasellus quis est sed[...]</p>
<div class="abs readmore">Read More »</div>
<div class="abs divider"></div>
<div class="abs news-img2" role="img" aria-label="DJ with raised arms under purple stage lights"></div>

<div class="abs footer-line"></div>
<footer class="abs footer"></footer>
<div class="abs bar-bottom"></div>

<h3 class="abs f-title" style="left:52px">Text Widget</h3>
<div class="abs f-text" style="left:52px"><p>Nam vestibulum, arcu sodales feugiat consectetur, nisl orci bibendum elit, eu euismod magna sapien ut nibh. Donec semper quam scelerisque.</p><p>Nam vestibulum, arcu sodales feugiat consectetur, nisl orci bibendum elit, eu euismod magna sapien ut nibh. Donec semper quam scelerisque.</p></div>

<h3 class="abs f-title" style="left:332px">Snapfeed</h3>
<div class="abs thumb" style="left:332px;top:2000px" role="img" aria-label="Gallery photo"></div>
<div class="abs thumb" style="left:419px;top:2000px" role="img" aria-label="Gallery photo"></div>
<div class="abs thumb" style="left:505px;top:2000px" role="img" aria-label="Gallery photo"></div>
<div class="abs thumb" style="left:332px;top:2086px" role="img" aria-label="Gallery photo"></div>
<div class="abs thumb" style="left:419px;top:2086px" role="img" aria-label="Gallery photo"></div>
<div class="abs thumb" style="left:505px;top:2086px" role="img" aria-label="Gallery photo"></div>
<div class="abs thumb" style="left:332px;top:2172px" role="img" aria-label="Gallery photo"></div>
<div class="abs thumb" style="left:419px;top:2172px" role="img" aria-label="Gallery photo"></div>
<div class="abs thumb" style="left:505px;top:2172px" role="img" aria-label="Gallery photo"></div>

<h3 class="abs f-title" style="left:612px">Text Widget</h3>
<div class="abs f-text" style="left:612px"><p>Nam vestibulum, arcu sodales feugiat consectetur, nisl orci bibendum elit, eu euismod magna sapien ut nibh. Donec semper quam scelerisque.</p><p>Nam vestibulum, arcu sodales feugiat consectetur, nisl orci bibendum elit, eu euismod magna sapien ut nibh. Donec semper quam scelerisque.</p></div>

<h3 class="abs f-title" style="left:895px">Text Widget</h3>
<table class="abs cal">
  <caption>June 2013</caption>
  <tr><th>M</th><th>T</th><th>W</th><th>T</th><th>F</th><th>S</th><th>S</th></tr>
  <tr><td></td><td></td><td></td><td></td><td></td><td>1</td><td>2</td></tr>
  <tr><td>3</td><td>4</td><td>5</td><td>6</td><td>7</td><td>8</td><td>9</td></tr>
  <tr><td>10</td><td>11</td><td>12</td><td>13</td><td>14</td><td>15</td><td>16</td></tr>
  <tr><td>17</td><td>18</td><td>19</td><td>20</td><td>21</td><td>22</td><td>23</td></tr>
  <tr><td>24</td><td>25</td><td>26</td><td>27</td><td>28</td><td>29</td><td>30</td></tr>
  <tr><td class="prev" colspan="2">Oct</td><td colspan="5"></td></tr>
</table>
</body>
</html>
```